Velnora Engineering Consulting

We need a website design for a new company based in South Africa called Brundel Consulting, it is a formidable engineering and consulting company with a background in Electrical and Mechanical design.We adopt a problem-solving methodology which allows us to present our clients with quick and flexible results. We offer complete engineering solutions from consulting, engineering design and even supply of equipment.
Target Market(s)
Government, private sector and public sector
Industry/Entity Type
Engineering Consulting
Number of Pages Required
5+ page
Colors
Designer to choose colors to be used in the design.
Requirements
Must have
- Must match the design of the profile, must enhance the profile look
Nice to have
- lates in terms of website design
Should not have
- Should be clean as the profile, should not deviate from the feel of the profile

```html
<!DOCTYPE html>
<html lang="en">
<head>
<meta charset="utf-8">
<title>Brundel Consulting</title>
<link rel="stylesheet" href="https://fonts.googleapis.com/css2?family=Montserrat:wght@500;600;700&family=Poppins:wght@300;400;500&display=swap">
<style>
:root{
  --teal:#1fb7a6;
  --navy:#1f2a36;
  --ink:#111418;
  --text:#5a5f66;
  --grey-bg:#f1f1f1;
  --white:#ffffff;
  --footer:#0b0b0b;
}
*{margin:0;padding:0;box-sizing:border-box}
html,body{width:1200px;height:3734px;overflow:hidden;background:var(--white)}
body{position:relative;font-family:'Poppins',sans-serif;color:var(--text)}
.abs{position:absolute}
h1,h2,h3,.brand{font-family:'Montserrat',sans-serif}
.photo{position:absolute}
.btn{position:absolute;display:flex;align-items:center;justify-content:center;font-family:'Montserrat',sans-serif;font-weight:600;font-size:16px;color:var(--white);background:var(--navy)}

/* hero */
.hero-photo{left:0;top:0;width:1200px;height:640px;background:linear-gradient(120deg,#0e2a3c 0%,#23485d 35%,#4a4038 55%,#152a3a 100%)}
.hero-edge{left:0;top:0}
.brand-logo{left:125px;top:52px;display:flex;align-items:center;gap:10px;color:var(--white);font-size:24px;font-weight:600;letter-spacing:1px}
.brand-logo .mark{width:22px;height:22px;border:2px solid var(--white)}
.burger{left:1040px;top:55px;width:28px}
.burger span{display:block;height:4px;background:var(--white);margin-bottom:5px}
.hero-title{right:110px;top:180px;text-align:right;color:var(--white);font-size:52px;font-weight:700;line-height:62px}
.hero-sub{right:110px;top:318px;text-align:right;color:var(--white);font-size:21px;line-height:38px}
.hero-btn{left:937px;top:415px;width:152px;height:45px;background:transparent;border:2px solid var(--white)}
.dots{left:1128px;top:268px}
.dots i{display:block;width:12px;height:12px;border-radius:50%;background:var(--white);margin:0 auto 18px}
.dots i.on{width:26px;height:26px;border:3px solid var(--white);background:transparent;position:relative}
.dots i.on::after{content:"";position:absolute;left:5px;top:5px;width:10px;height:10px;border-radius:50%;background:var(--white)}

/* about */
.about-frame{left:130px;top:760px;width:350px;height:410px;background:var(--navy)}
.about-photo{left:157px;top:740px;width:348px;height:410px;background:linear-gradient(160deg,#d9d3c4,#f1efe9 55%,#c8c3b8)}
.about-title{left:572px;top:752px;font-size:44px;font-weight:600;color:var(--ink)}
.about-text{left:572px;top:822px;width:494px;font-size:15px;line-height:27px;text-align:justify}
.about-text p{margin-bottom:8px}
.about-btn{left:572px;top:1120px;width:156px;height:48px}

/* products */
.prod-bg{left:0;top:1260px}
.prod-photo{left:0;top:1305px;width:1200px;height:365px;background:linear-gradient(90deg,#2a2b2c,#4d4a45 40%,#3a3a3b 70%,#5a5650)}
.prod-title{left:0;width:1200px;top:1360px;text-align:center;color:var(--white);font-size:38px;font-weight:700}
.tabs{left:355px;top:1432px;display:flex;gap:80px;color:var(--white);font-size:17px}
.tabs .active{border-bottom:2px solid var(--white);padding-bottom:6px}
.card{position:absolute;top:1505px;width:318px;height:335px;background:var(--white);box-shadow:0 2px 8px rgba(0,0,0,.18);text-align:center}
.card .photo{left:10px;top:10px;width:298px;height:155px}
.card h3{position:absolute;top:194px;width:100%;font-size:19px;font-weight:600;color:#333}
.card p{position:absolute;top:232px;left:24px;right:24px;font-size:13px;line-height:25px}
.arrow{position:absolute;top:1650px;width:38px;height:38px;border-radius:50%;background:var(--white);box-shadow:0 1px 5px rgba(0,0,0,.3)}

/* consulting */
.cons-photo{left:112px;top:1983px;width:473px;height:347px;background:linear-gradient(135deg,#7d8790,#c9ccce 45%,#8f969c);box-shadow:0 2px 8px rgba(0,0,0,.2)}
.cons-title{left:635px;top:1982px;font-size:34px;font-weight:700;color:var(--ink)}
.cons-text{left:638px;top:2038px;width:450px;font-size:14px;line-height:26px}
.checks{left:638px;top:2160px;list-style:none;font-size:15px;color:#333}
.checks li{display:flex;align-items:center;gap:12px;height:30px}
.cons-btn{left:640px;top:2265px;width:155px;height:46px}

/* industries */
.grey{left:0;top:2415px;width:1200px;height:900px;background:var(--grey-bg)}
.ind-title{left:0;width:1200px;top:2500px;text-align:center;font-size:38px;font-weight:700;color:var(--ink)}
.tile{position:absolute;width:310px;height:195px}
.tile-label{position:absolute;inset:0;display:flex;align-items:center;justify-content:center;color:var(--white);font-family:'Montserrat',sans-serif;font-size:30px;font-weight:600}
.acc-title{left:0;width:1200px;top:3075px;text-align:center;font-size:38px;font-weight:700;color:var(--ink)}
.badge{left:480px;top:3150px;width:240px;height:100px;border-radius:6px;background:#b8b8b8}

/* footer */
.footer-bg{left:0;top:3290px}
.f-brand{left:160px;top:3460px;color:var(--white);font-size:26px}
.f-col{position:absolute;top:3415px;color:var(--white)}
.f-col h3{font-size:20px;font-weight:600;margin-bottom:22px}
.f-col p,.f-col li{font-size:12px;line-height:20px}
.f-col ul{list-style:none}
.f-col li{line-height:27px}
.f-label{font-size:11px;margin-top:28px;padding-bottom:6px;border-bottom:1px solid #666;width:165px}
.f-btn{position:static;margin-top:28px;width:113px;height:34px;background:var(--teal);font-size:14px}
.contact{list-style:none}
.contact li{display:flex;gap:14px;align-items:flex-start;margin-bottom:20px;font-size:13px;line-height:22px}
.copyright{left:115px;top:3680px;color:var(--white);font-size:12px}
.social{left:928px;top:3672px;display:flex;gap:16px;align-items:center}
.social i{display:block;width:10px;height:10px;border-radius:50%;background:var(--white)}
.social i.big{width:26px;height:26px;background:var(--teal)}
</style>
</head>
<body>

<!-- hero -->
<div class="photo hero-photo" role="img" aria-label="Engineer working at monitors in a control room"></div>
<svg class="abs hero-edge" width="1200" height="700" viewBox="0 0 1200 700">
  <polygon points="0,553 870,640 1200,560 1200,700 0,700" fill="var(--teal)"/>
  <polygon points="0,570 870,652 1200,572 1200,700 0,700" fill="var(--white)"/>
</svg>
<div class="abs brand brand-logo"><span class="mark"></span>BRUNDEL</div>
<div class="abs burger"><span></span><span></span><span></span></div>
<h1 class="abs hero-title">Brundel Formidable<br>Engineering</h1>
<p class="abs hero-sub">Lorem ipsum dolor sit amet, consectetur adipiscing<br>elit,sed do eiusmod tempor incididunt</p>
<div class="btn hero-btn">Read More</div>
<div class="abs dots"><i class="on"></i><i></i><i></i></div>

<!-- about -->
<div class="abs about-frame"></div>
<div class="photo about-photo" role="img" aria-label="Engineer in hard hat reviewing plans"></div>
<h2 class="abs about-title">About Us</h2>
<div class="abs about-text">
  <p>With over 15 years combined experience in Engineering and Electrical Technology, we create solutions of the highest innovative standard.</p>
  <p>Established in 2014, Brundel Consulting is a formidable engineering and consulting company with a background in Electrical and Mechanical design. We adopt a problem-solving methodology which allows us to present our clients with quick and flexible results. We offer complete engineering solutions from consulting, engineering design and even supply of equipment.</p>
</div>
<div class="btn about-btn">Read More</div>

<!-- products -->
<svg class="abs prod-bg" width="1200" height="460" viewBox="0 0 1200 460">
  <polygon points="0,0 1200,45 0,45" fill="var(--teal)"/>
  <polygon points="1090,410 1200,410 1200,455" fill="var(--teal)"/>
</svg>
<div class="photo prod-photo" role="img" aria-label="Technician operating workshop machinery"></div>
<h2 class="abs prod-title">Products &amp; Services</h2>
<div class="abs tabs"><span class="active">Engineering &amp; Installation</span><span>Electrical Design</span></div>

<div class="card" style="left:112px">
  <div class="photo" style="background:linear-gradient(135deg,#9aa3aa,#e7e9ea)" role="img" aria-label="Engineer at a laptop in an office"></div>
  <h3>Project Management</h3>
  <p>Lorem ipsum dolor sit amet, consectetur adipiscing elit, sed do eiusmod tempor incididunt ut labore et</p>
</div>
<div class="card" style="left:441px">
  <div class="photo" style="background:linear-gradient(135deg,#cfd3d2,#f3f3f1)" role="img" aria-label="Team reviewing drawings at a desk"></div>
  <h3>Commissioning</h3>
  <p>Lorem ipsum dolor sit amet, consectetur adipiscing elit, sed do eiusmod tempor incididunt ut labore et</p>
</div>
<div class="card" style="left:770px">
  <div class="photo" style="background:linear-gradient(135deg,#3c4750,#8a8f93)" role="img" aria-label="Technician at industrial equipment"></div>
  <h3>Equipment supply</h3>
  <p>Lorem ipsum dolor sit amet, consectetur adipiscing elit, sed do eiusmod tempor incididunt ut labore et</p>
</div>
<div class="arrow" style="left:80px"><svg width="38" height="38"><path d="M21 13l-6 6 6 6" stroke="#333" stroke-width="2" fill="none"/></svg></div>
<div class="arrow" style="left:1082px"><svg width="38" height="38"><path d="M17 13l6 6-6 6" stroke="#333" stroke-width="2" fill="none"/></svg></div>

<!-- consulting -->
<div class="photo cons-photo" role="img" aria-label="Engineers pointing at technical plans on a table"></div>
<h2 class="abs cons-title">Brundel Consulting Services</h2>
<p class="abs cons-text">Sed ut perspiciatis unde omnis iste natus error sit voluptatem accusantium doloremque laudantium, totam rem aperiam, eaque ipsa quae ab illo inventore veritatis et quasi architecto beatae vitae dicta sunt explicabo.</p>
<ul class="abs checks">
  <li><svg width="14" height="14"><path d="M2 7l3.5 4L12 2" stroke="#222" stroke-width="2.5" fill="none"/></svg>Design Reviews</li>
  <li><svg width="14" height="14"><path d="M2 7l3.5 4L12 2" stroke="#222" stroke-width="2.5" fill="none"/></svg>Technical Advice</li>
  <li><svg width="14" height="14"><path d="M2 7l3.5 4L12 2" stroke="#222" stroke-width="2.5" fill="none"/></svg>Execution</li>
</ul>
<div class="btn cons-btn">Read More</div>

<!-- industries -->
<div class="abs grey"></div>
<h2 class="abs ind-title">Industries We Serve</h2>
<div class="tile" style="left:112px;top:2595px;background:linear-gradient(135deg,#1c3b52,#4f6e82)" role="img" aria-label="Engineer at monitors"></div>
<div class="tile" style="left:445px;top:2595px;background:linear-gradient(135deg,#3a3a3a,#6c6a66)" role="img" aria-label="Mining site with heavy truck"><span class="tile-label">Mining</span></div>
<div class="tile" style="left:778px;top:2595px;background:linear-gradient(135deg,#b0652a,#3d3b3a)" role="img" aria-label="Automotive engine and diagnostics"></div>
<div class="tile" style="left:112px;top:2805px;background:linear-gradient(135deg,#556069,#b7bcc0)" role="img" aria-label="Technician in a workshop"></div>
<div class="tile" style="left:445px;top:2805px;background:linear-gradient(135deg,#233140,#c99a3a)" role="img" aria-label="Dump truck at a night worksite"></div>
<div class="tile" style="left:778px;top:2805px;background:linear-gradient(135deg,#cfcac0,#f2f0ec)" role="img" aria-label="Engineer in hard hat with plans"></div>

<h2 class="abs acc-title">Accreditation Bodies</h2>
<div class="abs badge"></div>

<!-- footer -->
<svg class="abs footer-bg" width="1200" height="444" viewBox="0 0 1200 444">
  <polygon points="0,45 330,0 1200,60 1200,444 0,444" fill="var(--teal)"/>
  <polygon points="0,58 330,12 1200,72 1200,444 0,444" fill="var(--footer)"/>
</svg>
<div class="abs brand f-brand">BRUNDEL</div>
<div class="f-col" style="left:402px;width:180px">
  <h3>Newsletter</h3>
  <p>Subscribe to us to get and receive the latest news, sales and updates.</p>
  <div class="f-label">Email Address</div>
  <div class="btn f-btn">Sign Up</div>
</div>
<div class="f-col" style="left:645px">
  <h3>Links</h3>
  <ul><li>Home</li><li>About</li><li>Products &amp; Services</li><li>Brundel Consulting Services</li><li>Industries We Serve</li><li>Accreditation Bodies</li></ul>
</div>
<div class="f-col" style="left:862px">
  <h3>Contact Us</h3>
  <ul class="contact">
    <li><svg width="18" height="22"><path d="M9 21s7-7 7-12a7 7 0 0 0-14 0c0 5 7 12 7 12z" stroke="#fff" fill="none" stroke-width="1.5"/><circle cx="9" cy="9" r="2.5" stroke="#fff" fill="none"/></svg><span>14 Aloe Street, Brightvale,<br>Sandton, 2196, South Africa</span></li>
    <li><svg width="18" height="20"><path d="M4 2l4 4-2 3c1 2 3 4 5 5l3-2 4 4-3 3C8 18 1 10 1 5z" stroke="#fff" fill="none" stroke-width="1.4"/></svg><span>+27 (0) 60 555 0142</span></li>
    <li><svg width="20" height="16"><rect x="1" y="2" width="18" height="12" stroke="#fff" fill="none" stroke-width="1.4"/><path d="M1 2l9 7 9-7" stroke="#fff" fill="none" stroke-width="1.4"/></svg><span>info@brundelcs.com</span></li>
  </ul>
</div>
<p class="abs copyright">Copyright © 2019 &nbsp;|&nbsp; All Rights are Reserved.</p>
<div class="abs social"><i></i><i class="big"></i><i></i><i></i></div>

</body>
</html>
```